Stationary - Business Card/Letterhead and envelope design

Details for my new Stationery Design Project will be added soon. , I have two logos I am trying to decide on. I will upload the eps logos shortly. I have attached a file of what i have so far. I need urgently Business cards, but also will need a letterhead template and envelopes.

PLEASE NOTE THE DEADLINE SAYS 2 DAYS but I need business card design in LESS THAN A DAY.

thanks, Details for my new Stationery Design Project will be added soon. , I have two logos I am trying to decide on. I will upload the eps logos shortly. I have attached a file of what i have so far. I need urgently Business cards, but also will need a letterhead template and envelopes.

thanks
Updates

I have uploaded one of the logos you can work with. hopefully the other one comes soon.

details for the business card.

Marla Thorne

Managing Director

P&K Ventures Ltd

Bda: 1-441-555-0193

Email: marla@pkvnbda.com

web: www.pkvnbda.com

Industry/Entity Type

Business

```html
<!DOCTYPE html>
<html lang="en">
<head>
<meta charset="utf-8">
<title>P&amp;K Ventures – Business Card</title>
<link href="https://fonts.googleapis.com/css2?family=Montserrat:wght@400;600&display=swap" rel="stylesheet">
<style>
  :root {
    --backdrop: #ececec;
    --card: #ffffff;
    --teal: #2fa9b9;
    --brown: #85705c;
    --ink: #8a8a8a;
    --ink-dark: #6f6f6f;
  }
  * { margin: 0; padding: 0; box-sizing: border-box; }
  html, body {
    width: 1200px; height: 900px; overflow: hidden;
    background: var(--backdrop);
    font-family: "Montserrat", Arial, sans-serif;
  }
  .canvas {
    position: relative; width: 1200px; height: 900px;
  }
  .card {
    position: absolute; top: 298px;
    width: 530px; height: 303px;
    background: var(--card);
    box-shadow: 0 2px 10px rgba(0,0,0,0.08);
    overflow: hidden;
  }
  .card-front { left: 50px; }
  .card-back { left: 620px; }

  /* Front */
  .front-brand {
    position: absolute; left: 0; right: 0; top: 0; bottom: 0;
    display: flex; align-items: center; justify-content: center;
    gap: 16px;
  }
  .front-brand .brand-name {
    font-weight: 600; font-size: 54px; color: var(--teal);
    letter-spacing: 1px;
  }
  .brand-dot {
    width: 22px; height: 22px; background: var(--brown);
  }

  /* Back */
  .back-brand {
    position: absolute; top: 30px; left: 0; right: 0;
    text-align: center;
    font-weight: 600; font-size: 26px; color: var(--teal);
    letter-spacing: 0.5px;
  }
  .address {
    position: absolute; left: 26px; top: 100px;
    font-size: 11px; line-height: 17px; color: var(--ink);
  }
  .band-teal {
    position: absolute; left: 0; top: 160px;
    width: 265px; height: 10px; background: var(--teal);
  }
  .band-brown {
    position: absolute; left: 265px; top: 170px;
    width: 265px; height: 10px; background: var(--brown);
  }
  .person {
    position: absolute; right: 26px; top: 196px;
    text-align: right; color: var(--ink);
  }
  .person-name { font-size: 15px; color: var(--teal); }
  .person-title { font-size: 11px; margin-top: 2px; margin-bottom: 8px; }
  .contact-line {
    display: flex; align-items: center; justify-content: flex-end;
    gap: 6px; font-size: 11px; line-height: 17px;
  }
  .contact-line svg { width: 11px; height: 11px; }
  .email {
    position: absolute; left: 280px; top: 280px;
    font-size: 11px; color: var(--ink);
  }
</style>
</head>
<body>
<div class="canvas">
  <section class="card card-front">
    <div class="front-brand">
      <span class="brand-name">P&amp;K Ventures</span>
      <span class="brand-dot"></span>
    </div>
  </section>

  <section class="card card-back">
    <div class="back-brand">P&amp;K Ventures</div>

    <div class="address">
      42 Harbour Road<br>
      Hamilton, Bermuda HM 11<br>
      www.pkvnbda.com
    </div>

    <div class="band-teal"></div>
    <div class="band-brown"></div>

    <div class="person">
      <div class="person-name">Marla Thorne</div>
      <div class="person-title">managing director</div>
      <div class="contact-line">
        <span>1-441-555-0193</span>
        <svg viewBox="0 0 12 12"><path d="M3 1 L5 3.5 L4 5 Q5.5 7.5 7 8 L8.5 7 L11 9 L9.5 11 Q4 10 1 3 Z" fill="var(--brown)"/></svg>
      </div>
      <div class="contact-line">
        <span>1-441-555-0148</span>
        <svg viewBox="0 0 12 12"><rect x="3" y="0.5" width="6" height="11" rx="1" fill="var(--teal)"/><rect x="4" y="2" width="4" height="7" fill="#fff"/></svg>
      </div>
    </div>

    <div class="email">marla@pkvnbda.com</div>
  </section>
</div>
</body>
</html>
```